Emergency Dental Referral Company

I need a brochure to advertise my business to prospective dentists that may want to join or to dentists that may want to use this for their own patients. I also need to advertise this brochure to ER physicians who see many dental emergencies. This brochure is meant to be dual purpose: advertise our company and services to the ER physicians who then hand out the brochures to the dental emergency patients in pain. See our website for further details at www.molarquickfix.com

I will also be attaching our logo design.

Target Market(s)

Emergency Room physicians and other medical personnel who will distribute these brochures to patients in dental pain and dental emergencies

Industry/Entity Type

Business

Font styles to use
Serif
Sans Serif

Requirements
Must have
• Must be simple! Must have a call to action- inspiration to go to website. Highlight our guarantee that states "If you are not seen by a dentist in 24 hours or less, you will receive your money back. Emphasis on the logo. Must discuss how we find a dentist in your zip code in three easy steps.
• For the color- please make similar to our website of www.molarquickfix.com
Nice to have
• Would like to state that this service can see patients at any hour of the day.
Should not have
• no contact information besides the URL. www.molarquickfix.com

```html
<!DOCTYPE html>
<html lang="en">
<head>
<meta charset="utf-8">
<title>Find a Dentist in 3 Easy Steps</title>
<link rel="stylesheet" href="https://fonts.googleapis.com/css2?family=Bebas+Neue&family=Open+Sans:wght@400;600;700&display=swap">
<style>
  :root {
    --brand-blue: #1c6fbf;
    --brand-green: #8cc11f;
    --ink: #1a1a1a;
    --paper: #ffffff;
    --line: #3a3a3a;
    --photo-light: #e9f1f6;
    --photo-mid: #b9cfdc;
    --photo-warm: #d8b7a4;
  }
  * { box-sizing: border-box; margin: 0; padding: 0; }
  html, body { width: 1200px; height: 802px; overflow: hidden; background: var(--paper); }
  body { font-family: "Open Sans", Arial, sans-serif; color: var(--ink); }

  .brochure { position: relative; width: 1200px; height: 802px; background: var(--paper); overflow: hidden; }

  .headline {
    position: absolute; top: 36px; left: 62px; right: 40px;
    font-family: "Bebas Neue", "Oswald", sans-serif;
    font-size: 104px; line-height: 1; letter-spacing: 1px;
    display: flex; justify-content: space-between;
  }
  .headline-lead { color: var(--brand-blue); }
  .headline-accent { color: var(--brand-green); }

  .site-url {
    position: absolute; top: 124px; left: 66px;
    font-size: 15px; font-weight: 700; color: var(--brand-blue);
  }

  .steps-line { position: absolute; top: 242px; left: 40px; width: 1130px; height: 2px; background: var(--line); }

  .step { position: absolute; top: 165px; }
  .step-number { font-size: 50px; font-weight: 400; line-height: 1; display: inline-block; vertical-align: bottom; }
  .step-title { font-size: 16px; font-weight: 700; display: inline-block; vertical-align: bottom; margin: 0 0 6px 2px; }
  .step-dot {
    position: absolute; top: 65px; left: -4px;
    width: 28px; height: 28px; border-radius: 50%;
    border: 2px solid var(--line); background: var(--paper);
  }
  .step-one { left: 94px; }
  .step-two { left: 494px; }
  .step-three { left: 899px; }

  .callout {
    position: absolute; background: var(--brand-green); color: var(--paper);
    font-size: 16px; line-height: 1.45; padding: 22px 18px;
    box-shadow: 3px 4px 6px rgba(0,0,0,0.3);
  }
  .callout::before {
    content: ""; position: absolute; top: -10px; left: 0;
    border-right: 14px solid transparent; border-bottom: 10px solid var(--brand-green);
  }
  .callout-one { left: 104px; top: 262px; width: 232px; height: 96px; }
  .callout-two { left: 500px; top: 258px; width: 242px; height: 140px; z-index: 2; padding-top: 16px; }
  .callout-three { left: 908px; top: 262px; width: 248px; height: 96px; }

  .photo-rule { position: absolute; top: 378px; left: 0; width: 1200px; height: 7px; background: var(--brand-blue); }

  .photo-area {
    position: absolute; top: 385px; left: 0; width: 1200px; height: 383px;
    background: linear-gradient(100deg, var(--photo-light) 0%, var(--photo-mid) 35%, var(--photo-warm) 62%, var(--photo-light) 100%);
  }

  .guarantee-band {
    position: absolute; top: 768px; left: 0; width: 1200px; height: 34px;
    background: var(--brand-blue); color: var(--paper);
    font-size: 20px; line-height: 34px; text-align: center;
  }
  .guarantee-band strong { font-weight: 700; }
</style>
</head>
<body>
  <main class="brochure">
    <h1 class="headline">
      <span class="headline-lead">Find a Dentist in</span>
      <span class="headline-accent">3 Easy Steps</span>
    </h1>
    <p class="site-url">www.molarquickfix.com</p>

    <div class="steps-line"></div>

    <div class="step step-one">
      <span class="step-number">1</span><span class="step-title">Fill out a Form</span>
      <span class="step-dot"></span>
    </div>
    <div class="step step-two">
      <span class="step-number">2</span><span class="step-title">Find a Dentist</span>
      <span class="step-dot"></span>
    </div>
    <div class="step step-three">
      <span class="step-number">3</span><span class="step-title">Get your appointment</span>
      <span class="step-dot"></span>
    </div>

    <p class="callout callout-one">We will need your Zip code and contact information.</p>
    <p class="callout callout-two">Opportunity to choose among the most profitable and the most qualified dentist in you area.</p>
    <p class="callout callout-three">Get your emergency appointment</p>

    <div class="photo-rule"></div>
    <div class="photo-area" role="img" aria-label="Photo of a dentist in mask and gloves examining a young woman patient in a dental chair"></div>

    <p class="guarantee-band">If you are not seen by a dentist in 24 hours or less, <strong>you will receive your money back.</strong></p>
  </main>
</body>
</html>
```